Clear Path Glass Fix Business Card Design Project

Clear Path Glass Fix partners with insurance companies to repair the rock chips and small cracks on automobile windshields.
Updates

Target Market(s)

Will Be placed on windshield with chips. Design to get them to call us.

Industry/Entity Type

Automotive

Contact Information for Business Card

The cards will be placed on windshields near chips in the glass. The FRONT should have a photo of a star type rock chip. Clear Path Glass Fix is happy to provide FREE* rock chip repairs 948 615-2270 The BACK of the card will read. *Clear Path has partnered with over 100 insurance companies to provide
FREE Rock chip repairs to over 80% of our clients.
Why would we do this?
- FOR YOUR VISION AND SAFETY FIRST.
- To prevent crack spreading resulting in a very expensive windshield replacement.
- To preserve your factory set windshield seal.
- To preserve the environment as windshields cannot be recycled.
- To restore the beauty of your vehicle.
ZERO deductible and ZERO effect on your future premiums. CALL TODAY and we will have you Clearing Path in a matter of minutes.

Colors

Designer to choose colors to be used in the design.

Requirements
Must have
• STAR CRACK
Nice to have
• The bullet points on the back could possibly be little star cracks.

```html
<!DOCTYPE html>
<html lang="en">
<head>
<meta charset="utf-8">
<title>Clear Path Glass Fix – Business Card</title>
<link rel="stylesheet" href="https://fonts.googleapis.com/css2?family=Roboto+Condensed:wght@400;700&display=swap">
<style>
  :root {
    --page-bg: #e9e7e4;
    --card-white: #ffffff;
    --ice-blue: #d6e8f5;
    --brand-red: #9c1c1f;
    --ink: #2b2b2b;
    --back-dark: #151a1a;
    --back-olive: #454c3a;
    --back-steel: #56687a;
    --back-text: #f2f2f2;
    --edge-blue: #3a4f8a;
  }
  * { box-sizing: border-box; margin: 0; padding: 0; }
  html, body { width: 1200px; height: 1200px; overflow: hidden; }
  body {
    background: var(--page-bg);
    font-family: "Roboto Condensed", "Arial Narrow", sans-serif;
    position: relative;
  }
  .card {
    position: absolute;
    left: 120px;
    width: 960px;
    height: 549px;
    overflow: hidden;
    box-shadow: 0 6px 18px rgba(0,0,0,0.25);
  }
  /* Front */
  .card-front { top: 36px; background: var(--card-white); }
  .chip-photo {
    position: absolute;
    left: 0; top: 60px;
    width: 600px; height: 489px;
    background: radial-gradient(ellipse at 55% 55%, var(--ice-blue) 0%, #eaf3fa 45%, rgba(255,255,255,0) 75%);
  }
  .front-glow {
    position: absolute;
    right: 0; top: 180px;
    width: 520px; height: 369px;
    background: radial-gradient(ellipse at 60% 60%, #e4eff8 0%, rgba(255,255,255,0) 70%);
  }
  .brand-name {
    position: absolute;
    left: 100px; top: 66px;
    width: 810px;
    text-align: center;
    font-weight: 700;
    font-size: 50px;
    line-height: 1;
    letter-spacing: 9px;
    color: var(--brand-red);
    text-transform: uppercase;
    white-space: nowrap;
  }
  .offer {
    position: absolute;
    left: 480px; width: 440px;
    text-align: center;
    color: var(--brand-red);
  }
  .offer-intro { top: 222px; font-size: 46px; }
  .offer-free { top: 290px; font-size: 76px; font-weight: 700; line-height: 1; }
  .offer-what { top: 370px; font-size: 44px; }
  .offer-phone { top: 432px; font-size: 58px; font-weight: 700; color: var(--ink); letter-spacing: 1px; }

  /* Back */
  .card-back {
    top: 615px;
    background:
      radial-gradient(ellipse at 30% 5%, var(--back-olive) 0%, rgba(69,76,58,0) 45%),
      radial-gradient(ellipse at 5% 100%, var(--back-steel) 0%, rgba(86,104,122,0) 45%),
      radial-gradient(ellipse at 75% 55%, #3c4448 0%, rgba(60,68,72,0) 40%),
      var(--back-dark);
    color: var(--back-text);
    border-bottom: 3px solid var(--edge-blue);
  }
  .crack-backdrop {
    position: absolute;
    left: 640px; top: 40px;
    width: 280px; height: 260px;
    background: radial-gradient(circle, rgba(180,185,185,0.35) 0%, rgba(180,185,185,0) 65%);
  }
  .back-content { position: absolute; left: 48px; top: 52px; width: 880px; }
  .partner-note { font-size: 25px; line-height: 1.3; }
  .why-heading { font-size: 34px; font-weight: 700; margin: 18px 0 10px 30px; }
  .reasons { list-style: none; margin-left: 24px; }
  .reasons li {
    display: flex; align-items: flex-start;
    font-size: 25px; line-height: 1.3;
    margin-bottom: 12px;
  }
  .reasons svg { flex: none; width: 42px; height: 38px; margin-right: 14px; margin-top: -4px; }
  .closing { text-align: center; font-size: 25px; line-height: 1.3; margin-top: 4px; }
</style>
</head>
<body>

<section class="card card-front">
  <div class="chip-photo" role="img" aria-label="Photo of a star-shaped rock chip crack in a windshield"></div>
  <div class="front-glow"></div>
  <div class="brand-name">Clear Path Glass Fix</div>
  <div class="offer offer-intro">Happy to provide</div>
  <div class="offer offer-free">FREE*</div>
  <div class="offer offer-what">ROCK CHIP REPAIRS</div>
  <div class="offer offer-phone">948 615-2270</div>
</section>

<section class="card card-back">
  <div class="crack-backdrop" role="img" aria-label="Faint photo of a rock chip crack on dark glass"></div>
  <div class="back-content">
    <p class="partner-note">*Clear Path has partnered with over 100 insurance companies to provide FREE Rock chip repairs to over 80% of our Clients.</p>
    <h2 class="why-heading">WHY WOULD WE DO THIS?</h2>
    <ul class="reasons">
      <li><svg viewBox="0 0 40 40"><polygon fill="#fff" points="20,0 23,15 38,6 26,18 40,22 25,24 33,38 21,27 17,40 16,26 3,35 13,22 0,17 14,15 6,3 18,13"/></svg>FOR YOUR VISION AND SAFETY FIRST.</li>
      <li><svg viewBox="0 0 40 40"><polygon fill="#fff" points="20,0 23,15 38,6 26,18 40,22 25,24 33,38 21,27 17,40 16,26 3,35 13,22 0,17 14,15 6,3 18,13"/></svg>To prevent a crack from spreading, resulting in a very expensive windshield replacement.</li>
      <li><svg viewBox="0 0 40 40"><polygon fill="#fff" points="20,0 23,15 38,6 26,18 40,22 25,24 33,38 21,27 17,40 16,26 3,35 13,22 0,17 14,15 6,3 18,13"/></svg>To preserve your factory set windshield seal.</li>
      <li><svg viewBox="0 0 40 40"><polygon fill="#fff" points="20,0 23,15 38,6 26,18 40,22 25,24 33,38 21,27 17,40 16,26 3,35 13,22 0,17 14,15 6,3 18,13"/></svg>To preserve the environment as windshields cannot be recycled.</li>
      <li><svg viewBox="0 0 40 40"><polygon fill="#fff" points="20,0 23,15 38,6 26,18 40,22 25,24 33,38 21,27 17,40 16,26 3,35 13,22 0,17 14,15 6,3 18,13"/></svg>To restore the beauty of your vehicle.</li>
    </ul>
    <p class="closing">ZERO deductible and ZERO effect on your future premiums.<br>CALL US TODAY and we will have you CLEARING PATH in a matter of minutes.</p>
  </div>
</section>

</body>
</html>
```